Ferncliff Aquatic Centre Open Day

FRONT PAGE

FERNCLIFF AQUATIC CENTRE OPEN DAY
31st May 2014
10am - 4pm
Free entry

Our Free Open Day is an event designed for the community to dive in and enjoy our great aquatic venue. There are plenty of activities for parents and kids to enjoy including the pool activities, free fitness classes and much more! Come join us on this great day to mark our 6 months of operation.

Sausage sizzle
pool activities
free group fitness classes
giveaways
door prizes

BACK PAGE
map of location
ph: 4735 2084
enquiries@fcswimhub.com.au

want fitness and aquatic pics

plenty of colour - DL size
in your face kind of flyer

```html
<!DOCTYPE html>
<html lang="en">
<head>
<meta charset="utf-8">
<title>Ferncliff Aquatic Centre Open Day</title>
<link rel="stylesheet" href="https://fonts.googleapis.com/css2?family=Luckiest+Guy&family=Lilita+One&family=Cinzel:wght@700&family=Montserrat:wght@600;700&family=Fredoka:wght@600&display=swap">
<style>
  :root {
    --page: #ececea;
    --teal: #3aa8c1;
    --teal-light: #6cc4d6;
    --teal-dark: #1d7d96;
    --teal-deep: #145f74;
    --orange: #f38a12;
    --yellow: #ffd23a;
    --grey: #9c9d9f;
    --white: #ffffff;
  }
  * { box-sizing: border-box; margin: 0; padding: 0; }
  html, body { width: 1200px; height: 1200px; overflow: hidden; }
  body { background: var(--page); position: relative; }

  .flyer {
    position: absolute; top: 102px; width: 486px; height: 974px; overflow: hidden;
    box-shadow: 0 4px 14px rgba(0,0,0,.25);
  }
  .flyer--front { left: 94px; background: linear-gradient(180deg, var(--teal) 0%, var(--teal-dark) 55%, var(--teal-dark) 100%); }
  .flyer--back { left: 606px; background: linear-gradient(180deg, var(--teal) 0%, var(--teal-light) 22%, var(--teal) 70%, var(--teal-dark) 100%); }
  .flyer svg.shape { position: absolute; left: 0; display: block; }

  .display {
    font-family: "Luckiest Guy", "Lilita One", cursive;
    text-transform: uppercase; line-height: 1; letter-spacing: 1px;
    color: var(--orange);
    background: linear-gradient(180deg, var(--yellow) 15%, var(--orange) 70%);
    -webkit-background-clip: text; background-clip: text; -webkit-text-fill-color: transparent;
    filter: drop-shadow(2px 0 0 #fff) drop-shadow(-2px 0 0 #fff) drop-shadow(0 2px 0 #fff) drop-shadow(0 -2px 0 #fff) drop-shadow(0 3px 4px rgba(0,0,0,.35));
  }

  /* front */
  .front__photo {
    position: absolute; left: 0; top: 560px; width: 486px; height: 290px;
    background: linear-gradient(180deg, rgba(29,125,150,0) 0%, #3a9dbb 30%, #2c8db0 65%, #1f7394 100%);
  }
  .front__glow {
    position: absolute; left: 0; top: 300px; width: 486px; height: 320px;
    background: radial-gradient(ellipse at 50% 40%, rgba(255,255,255,.28), rgba(255,255,255,0) 65%);
  }
  .front__brand {
    position: absolute; top: 62px; left: 0; width: 486px;
    display: flex; align-items: center; justify-content: center; gap: 14px;
  }
  .front__brand-mark { width: 22px; height: 22px; border-radius: 50%; background: var(--teal); }
  .front__brand-name {
    font-family: "Montserrat", sans-serif; font-weight: 700; color: var(--teal);
    font-size: 34px; line-height: 1.05; text-transform: uppercase; letter-spacing: 1px;
  }
  .front__title { position: absolute; top: 336px; left: 0; width: 486px; text-align: center; font-size: 76px; }
  .front__when {
    position: absolute; top: 420px; left: 0; width: 486px; text-align: center;
    font-family: "Fredoka", sans-serif; font-weight: 600; font-size: 24px; color: var(--yellow);
    text-shadow: 0 2px 3px rgba(0,0,0,.3);
  }
  .front__when span + span { margin-left: 34px; }
  .front__activities {
    position: absolute; top: 488px; left: 0; width: 486px; list-style: none; text-align: center;
    font-family: "Cinzel", serif; font-weight: 700; font-size: 21px; color: var(--white);
    text-transform: uppercase; letter-spacing: .5px;
    text-shadow: 0 1px 2px rgba(0,0,0,.6), 0 2px 6px rgba(0,0,0,.4);
  }
  .front__activities li { height: 51.5px; line-height: 32px; }
  .front__footer {
    position: absolute; left: 0; top: 848px; width: 486px; height: 126px;
    background: var(--grey); text-align: center;
  }
  .front__venue {
    margin-top: 30px; font-family: "Cinzel", serif; font-weight: 700; font-size: 17px; color: var(--white);
    text-transform: uppercase;
  }
  .front__entry {
    margin-top: 2px; font-family: "Cinzel", serif; font-weight: 700; font-size: 40px; color: var(--teal-deep);
    text-transform: uppercase;
    text-shadow: 1px 0 0 #fff, -1px 0 0 #fff, 0 1px 0 #fff, 0 -1px 0 #fff, 0 3px 4px rgba(0,0,0,.3);
  }

  /* back */
  .back__phone {
    position: absolute; top: 12px; left: 0; width: 486px; text-align: center;
    font-family: "Montserrat", sans-serif; font-weight: 700; font-size: 21px; letter-spacing: 2px;
    color: var(--white); text-shadow: 0 1px 3px rgba(0,0,0,.4);
  }
  .back__pass { position: absolute; top: 140px; left: 0; width: 486px; text-align: center; font-size: 48px; }
  .back__gallery {
    position: absolute; top: 204px; left: 0; width: 486px; height: 476px; background: var(--white);
  }
  .back__photo { position: absolute; }
  .back__photo--pool { left: 0; top: 8px; width: 282px; height: 248px; background: linear-gradient(180deg, #9fb9c9 0%, #5fa9c4 30%, #2f8fb0 60%, #c7ad85 85%); }
  .back__photo--weights { left: 296px; top: 8px; width: 190px; height: 248px; background: linear-gradient(135deg, #e79a86 0%, #8a7c7a 35%, #45474c 65%, #2a2b2f 100%); }
  .back__photo--gym { left: 0; top: 268px; width: 264px; height: 196px; background: linear-gradient(180deg, #cfcbc3 0%, #8f8d88 45%, #5a5956 100%); }
  .back__photo--splash { left: 278px; top: 268px; width: 208px; height: 196px; background: linear-gradient(180deg, #dfe6ea 0%, #9fc8d6 45%, #3e93b2 100%); }
  .back__features {
    position: absolute; top: 704px; left: 0; width: 486px; list-style: none; text-align: center;
    font-family: "Cinzel", serif; font-weight: 700; font-size: 13px; color: var(--white);
    text-transform: uppercase;
    text-shadow: 0 1px 2px rgba(0,0,0,.4);
  }
  .back__features li { height: 23.6px; line-height: 23.6px; }
  .back__email {
    position: absolute; top: 940px; left: 32px;
    font-family: "Montserrat", sans-serif; font-weight: 600; font-size: 15px; letter-spacing: 1px; color: var(--white);
  }
</style>
</head>
<body>

<section class="flyer flyer--front">
  <div class="front__photo" role="img" aria-label="Photo of an indoor lap pool with lane ropes under a curved roof"></div>
  <div class="front__glow"></div>

  <svg class="shape" style="top:0" width="486" height="340" viewBox="0 0 486 340" aria-hidden="true">
    <path d="M0 0H486V230C420 232 350 280 250 300C170 312 100 290 60 270C40 262 20 258 0 256Z" fill="var(--white)"/>
    <path d="M70 262C150 320 300 318 486 236V262C320 330 170 340 70 262Z" fill="var(--teal-dark)" opacity=".55"/>
  </svg>

  <div class="front__brand">
    <span class="front__brand-mark"></span>
    <span class="front__brand-name">Ferncliff<br>Aquatic Centre</span>
  </div>

  <h1 class="front__title display">Open Day</h1>
  <p class="front__when"><span>31ST MAY 2014</span><span>10AM - 4PM</span></p>

  <ul class="front__activities">
    <li>Sausage Sizzle</li>
    <li>Pool Activities</li>
    <li>Free Group Fitness Classes</li>
    <li>Giveaways</li>
    <li>Door Prizes</li>
  </ul>

  <svg class="shape" style="top:824px" width="486" height="30" viewBox="0 0 486 30" aria-hidden="true">
    <path d="M0 14L14 8L26 16L40 6L56 12L70 4L86 14L102 8L118 16L132 6L150 12L166 4L182 14L198 10L214 16L230 6L248 12L262 4L280 14L296 8L312 16L328 6L346 12L362 4L378 14L394 8L410 16L426 6L444 12L458 4L474 14L486 8V30H0Z" fill="var(--white)"/>
  </svg>

  <div class="front__footer">
    <p class="front__venue">Ferncliff Aquatic Centre</p>
    <p class="front__entry">Free Entry</p>
  </div>
</section>

<section class="flyer flyer--back">
  <svg class="shape" style="top:0" width="486" height="110" viewBox="0 0 486 110" aria-hidden="true">
    <path d="M0 0H486V58C380 44 300 56 220 74C140 92 60 90 0 74Z" fill="var(--teal-dark)"/>
    <path d="M0 74C60 90 140 92 220 74C300 56 380 44 486 58V66C380 54 300 66 220 84C140 102 60 98 0 84Z" fill="var(--teal-deep)" opacity=".7"/>
  </svg>
  <p class="back__phone">PHONE : 4735 2084</p>
  <h2 class="back__pass display">7 Day Pass</h2>

  <div class="back__gallery">
    <div class="back__photo back__photo--pool" role="img" aria-label="Photo of the indoor lap pool hall"></div>
    <div class="back__photo back__photo--weights" role="img" aria-label="Photo of a dumbbell rack in the gym"></div>
    <div class="back__photo back__photo--gym" role="img" aria-label="Photo of spin bikes and exercise balls in the fitness room"></div>
    <div class="back__photo back__photo--splash" role="img" aria-label="Photo of the splash pool with play features"></div>
  </div>

  <ul class="back__features">
    <li>State of the art fully equipped gym</li>
    <li>Group fitness classes</li>
    <li>Aqua aerobics</li>
    <li>Learn to swim program</li>
    <li>25 meter lap pool</li>
    <li>Program pool</li>
    <li>Splash pool</li>
    <li>We have something here for everyone</li>
  </ul>

  <svg class="shape" style="top:896px" width="486" height="78" viewBox="0 0 486 78" aria-hidden="true">
    <path d="M0 30C120 0 300 0 486 22V78H0Z" fill="var(--teal-deep)" opacity=".85"/>
    <path d="M0 38C120 10 300 10 486 30V78H0Z" fill="var(--teal)"/>
  </svg>
  <p class="back__email">enquiries@fcswimhub.com.au</p>
</section>

</body>
</html>
```